Career Management Consultant Fun Professional Business Card

This is a business card for a personal career management consultant. The vibe needs to be professional but fun, modern with colour.

The name of the business is "Marcus Telvorne Career Management Consulting"

The name of the individual is "Marcus Telvorne" and his title is "Career Management Consultant"

Contact Information for Business Card

Marcus Telvorne
Phone: 0400 731 862
Email: Marcus.Telvorne@quillmail.net

```html
<!DOCTYPE html>
<html lang="en">
<head>
<meta charset="utf-8">
<title>Marcus Telvorne – Business Card</title>
<link rel="stylesheet" href="https://fonts.googleapis.com/css2?family=Montserrat:wght@500;600&family=Quicksand:wght@400;500&display=swap">
<style>
  :root {
    --bg: #e9ebee;
    --paper: #ffffff;
    --paper-shade: #eef0f2;
    --navy: #0d5a86;
    --blue: #1479bd;
    --blue-light: #1b8ccc;
    --ink-name: #145a87;
    --ink-tag: #1b7fc1;
    --ink-light: #e6f1f8;
    --rule: rgba(255,255,255,0.18);
  }
  * { box-sizing: border-box; margin: 0; padding: 0; }
  html, body { width: 1200px; height: 1000px; overflow: hidden; }
  body {
    background: var(--bg);
    position: relative;
    font-family: "Quicksand", sans-serif;
  }
  .card {
    position: absolute;
    left: 220px;
    width: 760px;
    height: 420px;
    background: radial-gradient(ellipse at 45% 55%, var(--paper) 40%, var(--paper-shade) 100%);
    box-shadow: 0 6px 18px rgba(0,0,0,0.12);
    overflow: hidden;
  }
  .card--front { top: 50px; }
  .card--back { top: 530px; }
  .card__shapes { position: absolute; inset: 0; width: 100%; height: 100%; }

  .brand {
    position: absolute;
    display: flex;
    align-items: center;
    gap: 18px;
  }
  .brand__square {
    width: 54px; height: 54px;
    background: var(--blue);
    flex: none;
  }
  .brand__name {
    font-family: "Montserrat", sans-serif;
    font-weight: 600;
    font-size: 27px;
    color: var(--ink-name);
    letter-spacing: 0.5px;
    line-height: 1.1;
  }
  .brand__tagline {
    font-family: "Quicksand", sans-serif;
    font-weight: 500;
    font-size: 21px;
    color: var(--ink-tag);
    letter-spacing: 0.6px;
    line-height: 1.2;
  }
  .card--front .brand { left: 200px; top: 178px; }

  .card--back .brand { left: 40px; top: 292px; }
  .card--back .brand__name { font-size: 24px; }
  .card--back .brand__tagline { font-size: 18px; }

  .contact {
    position: absolute;
    right: 60px;
    top: 40px;
    width: 400px;
    color: var(--ink-light);
  }
  .contact__name {
    font-family: "Montserrat", sans-serif;
    font-weight: 500;
    font-size: 24px;
    text-align: right;
    letter-spacing: 0.5px;
  }
  .contact__title {
    font-size: 17px;
    text-align: right;
    margin-top: 4px;
    letter-spacing: 0.5px;
    opacity: 0.9;
  }
  .contact__list { list-style: none; margin-top: 22px; }
  .contact__item {
    display: flex;
    align-items: center;
    gap: 16px;
    height: 46px;
    border-top: 1px solid var(--rule);
    font-size: 19px;
    letter-spacing: 0.4px;
  }
  .contact__icon {
    width: 34px; height: 34px;
    background: var(--blue-light);
    display: flex; align-items: center; justify-content: center;
    flex: none;
  }
  .contact__icon svg { width: 18px; height: 18px; fill: #fff; }
</style>
</head>
<body>

  <section class="card card--front" aria-label="Business card front">
    <svg class="card__shapes" viewBox="0 0 760 420" preserveAspectRatio="none" aria-hidden="true">
      <polygon points="430,0 760,0 760,62" fill="var(--blue)"/>
    </svg>
    <div class="brand">
      <span class="brand__square"></span>
      <div>
        <p class="brand__name">Marcus Telvorne</p>
        <p class="brand__tagline">Career Management Consulting</p>
      </div>
    </div>
  </section>

  <section class="card card--back" aria-label="Business card back">
    <svg class="card__shapes" viewBox="0 0 760 420" preserveAspectRatio="none" aria-hidden="true">
      <polygon points="100,0 760,0 760,420 560,420" fill="var(--navy)"/>
      <polygon points="760,140 760,420 620,420" fill="var(--blue-light)"/>
    </svg>

    <div class="contact">
      <p class="contact__name">Marcus Telvorne</p>
      <p class="contact__title">Career Management Consultant</p>
      <ul class="contact__list">
        <li class="contact__item">
          <span class="contact__icon">
            <svg viewBox="0 0 24 24"><path d="M6.6 10.8a15.1 15.1 0 0 0 6.6 6.6l2.2-2.2a1 1 0 0 1 1-.25 11.4 11.4 0 0 0 3.6.57 1 1 0 0 1 1 1V20a1 1 0 0 1-1 1A17 17 0 0 1 3 4a1 1 0 0 1 1-1h3.5a1 1 0 0 1 1 1c0 1.25.2 2.45.57 3.57a1 1 0 0 1-.25 1z"/></svg>
          </span>
          <span>0400 731 862</span>
        </li>
        <li class="contact__item">
          <span class="contact__icon">
            <svg viewBox="0 0 24 24"><path d="M3 5h18v14H3z M4.5 6.5 12 12l7.5-5.5" fill="none" stroke="#fff" stroke-width="2"/></svg>
          </span>
          <span>Marcus.Telvorne@quillmail.net</span>
        </li>
      </ul>
    </div>

    <div class="brand">
      <span class="brand__square"></span>
      <div>
        <p class="brand__name">Marcus Telvorne</p>
        <p class="brand__tagline">Career Management Consulting</p>
      </div>
    </div>
  </section>

</body>
</html>
```